The Quiet Harbor book cover

To design an e-book and printed cover that will initially be used on Bookvale for Leafpad.

My website www.thequietharbor.example

Full title
The Quiet Harbor - Start your own success journey in '4 simple steps'.
Subtitle: Everything from understanding your subconscious mind to setting out an action plan for your future.

The Quiet harbor part although it's the beginning of the title will be the smaller part, the rest will be the focus.

I want a clean modern feel, take inspiration from the top self-help books currently on Bookvale. Clean crisp and bold.

The book is about setting goals and navigating a complicated road of obstacles in order to achieve them. If this can be illustrated in the graphic or on the cover that would be a bonus.

Requirements for the size of your cover art must have an ideal height/width ratio of at least 1.6, meaning:

• A minimum of 625 pixels on the shortest side and 1000 pixels on the longest side
• For best quality, your image should be 2500 pixels on the longest side

Reason: Going to go through last time give feedback and any changes before I pick 3 to get a poll done. Loving the ideas and designs. New designs welcome, please put all emphasis on the subheading 'start your...' Have a great Christmas if you celebrate.

Target Market(s)

Target market would be middle age male and females.

Industry/Entity Type

Moving

Font styles to use
Serif
Sans Serif

Requirements
Must have
• Must have the full title even if it is split.

Author name Dorian Falke
Nice to have
• The photo of author but not sure whether to use it or not.

Graphics like moving roads and suchlike.

```html
<!DOCTYPE html>
<html lang="en">
<head>
<meta charset="utf-8">
<title>The Quiet Harbor — Book Cover</title>
<link rel="stylesheet" href="https://fonts.googleapis.com/css2?family=Montserrat:ital,wght@0,500;0,600;1,800&family=Poiret+One&display=swap">
<style>
  :root {
    --page: #ffffff;
    --sky: #468ccb;
    --road: #000000;
    --title-red: #ee3b36;
    --ink-light: #ffffff;
    --motion-grey: #b9b9b9;
  }
  * { margin: 0; padding: 0; box-sizing: border-box; }
  html, body {
    width: 1000px;
    height: 1200px;
    overflow: hidden;
    background: var(--page);
  }
  .cover {
    position: relative;
    width: 1000px;
    height: 1200px;
    background: var(--page);
  }
  .cover__backdrop {
    position: absolute;
    left: 125px;
    top: 0;
    width: 750px;
    height: 1200px;
    background: var(--sky);
  }
  .cover__road {
    position: absolute;
    left: 0;
    top: 0;
  }
  .series-title {
    position: absolute;
    top: 132px;
    left: 0;
    width: 1056px;
    text-align: center;
    font-family: "Montserrat", sans-serif;
    font-weight: 500;
    font-size: 36px;
    letter-spacing: 4px;
    color: var(--title-red);
    white-space: nowrap;
  }
  .series-title__motion {
    display: inline-block;
    font-style: italic;
    font-weight: 800;
    color: var(--motion-grey);
    filter: blur(1.6px);
    letter-spacing: 2px;
    margin: 0 4px;
  }
  .lead-in {
    position: absolute;
    top: 228px;
    left: 0;
    width: 1000px;
    text-align: center;
    font-family: "Poiret One", sans-serif;
    color: var(--ink-light);
    font-size: 26px;
    line-height: 31px;
  }
  .lead-in__line { display: block; }
  .lead-in__line--in { font-size: 32px; line-height: 40px; }
  .headline {
    position: absolute;
    left: 0;
    width: 1000px;
    text-align: center;
    font-family: "Poiret One", sans-serif;
    color: var(--ink-light);
    line-height: 1;
  }
  .headline--number { top: 420px; font-size: 230px; }
  .headline--simple { top: 630px; font-size: 118px; letter-spacing: 2px; }
  .headline--steps { top: 777px; font-size: 150px; letter-spacing: 2px; }
  .author {
    position: absolute;
    left: 0;
    width: 1000px;
    text-align: center;
    font-family: "Montserrat", sans-serif;
    font-weight: 600;
    color: var(--ink-light);
    line-height: 1;
  }
  .author--first { top: 1020px; font-size: 42px; letter-spacing: 12px; padding-left: 12px; }
  .author--last { top: 1078px; font-size: 44px; letter-spacing: 16px; padding-left: 16px; }
</style>
</head>
<body>
  <main class="cover">
    <div class="cover__backdrop"></div>
    <svg class="cover__road" width="1000" height="1200" viewBox="0 0 1000 1200" aria-hidden="true">
      <polygon points="432,0 567,0 748,1200 253,1200" fill="var(--road)"/>
    </svg>

    <h1 class="series-title">THE <span class="series-title__motion">QUIET</span> HARBOR:</h1>

    <p class="lead-in">
      <span class="lead-in__line">Start</span>
      <span class="lead-in__line">your</span>
      <span class="lead-in__line">own</span>
      <span class="lead-in__line">success</span>
      <span class="lead-in__line">journey</span>
      <span class="lead-in__line lead-in__line--in">in</span>
    </p>

    <div class="headline headline--number">4</div>
    <div class="headline headline--simple">SIMPLE</div>
    <div class="headline headline--steps">STEPS</div>

    <div class="author author--first">Dorian</div>
    <div class="author author--last">FALKE</div>
  </main>
</body>
</html>
```